BM banner

we need a banner design (36"x120" horizontal) that will be displayed on a local high school baseball field. My company ( Quill Pennant Co) has been producing signage for the Birch Meadows community since 2009. We would like to communicate that we do more than banners. The final design should include the slogan "Signs Shirts Swag" and our Logo.

Target Market(s)

companies, teams, events, shirt and other marketing items.

Industry/Entity Type

Sign, Print,

Font styles to use
Sans Serif

Requirements
Should not have
• no baseball content.

```html
<!DOCTYPE html>
<html lang="en">
<head>
<meta charset="utf-8">
<title>Quill Pennant Co — Field Banner</title>
<link rel="stylesheet" href="https://fonts.googleapis.com/css2?family=Bebas+Neue&family=Montserrat:wght@300;700&display=swap">
<style>
  :root {
    --backdrop: #dcdcdc;
    --ink: #000000;
    --paper: #ffffff;
  }
  * { box-sizing: border-box; margin: 0; padding: 0; }
  html, body {
    width: 1200px;
    height: 851px;
    overflow: hidden;
    background: var(--backdrop);
  }
  .banner {
    position: absolute;
    left: 105px;
    top: 260px;
    width: 990px;
    height: 296px;
    display: flex;
  }
  .brand-panel {
    width: 347px;
    background: var(--paper);
    display: flex;
    flex-direction: column;
    align-items: center;
    justify-content: space-between;
    padding: 34px 20px 20px;
  }
  .brand-mark {
    flex: 1;
    display: flex;
    align-items: center;
    gap: 14px;
  }
  .brand-square {
    width: 46px;
    height: 46px;
    background: var(--ink);
    flex-shrink: 0;
  }
  .brand-name {
    font-family: "Montserrat", sans-serif;
    font-weight: 700;
    font-size: 27px;
    line-height: 1.1;
    color: var(--ink);
  }
  .brand-url {
    font-family: "Montserrat", sans-serif;
    font-weight: 700;
    font-size: 23px;
    color: var(--ink);
    letter-spacing: 0.2px;
  }
  .slogan-panel {
    flex: 1;
    background: var(--ink);
    display: flex;
    flex-direction: column;
    align-items: center;
    justify-content: center;
    padding: 0 50px 60px 58px;
  }
  .slogan {
    font-family: "Bebas Neue", sans-serif;
    font-size: 92px;
    line-height: 1;
    color: var(--paper);
    letter-spacing: 1px;
    white-space: nowrap;
  }
  .established {
    width: 100%;
    display: flex;
    align-items: center;
    gap: 10px;
    margin-top: 8px;
  }
  .established-rule {
    flex: 1;
    height: 2px;
    background: var(--paper);
  }
  .established-text {
    font-family: "Montserrat", sans-serif;
    font-weight: 300;
    font-size: 18px;
    color: var(--paper);
  }
</style>
</head>
<body>
  <section class="banner">
    <div class="brand-panel">
      <div class="brand-mark">
        <span class="brand-square"></span>
        <span class="brand-name">Quill Pennant Co</span>
      </div>
      <p class="brand-url">QuillPennantCo.com</p>
    </div>
    <div class="slogan-panel">
      <h1 class="slogan">Signs Shirts Swag</h1>
      <div class="established">
        <span class="established-rule"></span>
        <span class="established-text">Est.2009</span>
        <span class="established-rule"></span>
      </div>
    </div>
  </section>
</body>
</html>
```